Commercial and Multifamily informational website

We need a website for our commercial real estate management company. We will manage offices, retail, apartments and others. Here is the brief verbiage: Providing quality commercial and multifamily portfolio management to Landlords, REITs, and financial institutions. 

Industry/Entity Type

Real Estate

Number of Pages Required

2 page

Font styles to use
Sans Serif
Other font styles liked:
• Muli, Garamond

Colors
0555a3
5c5c5c
3176b5
85acd3
474747

Requirements
Must have
• Home page and contact page

```html
<!DOCTYPE html>
<html lang="en">
<head>
<meta charset="utf-8">
<title>Norvale Property Management</title>
<link rel="stylesheet" href="https://fonts.googleapis.com/css2?family=Arimo:wght@400;700&family=Montserrat:wght@300;400;600;700&family=Roboto+Condensed:wght@300;400;700&family=EB+Garamond:wght@500&family=Open+Sans:wght@400;600&display=swap">
<style>
:root{
  --navy:#0555a3;
  --deep:#0b3470;
  --ink:#1c2f5c;
  --grey:#5c5c5c;
  --charcoal:#474747;
  --mid:#3176b5;
  --sky:#85acd3;
  --light:#f2f3f4;
  --footer:#353535;
  --text:#333;
}
*{box-sizing:border-box;margin:0;padding:0}
html,body{width:1200px;height:3303px;overflow:hidden}
body{position:relative;background:#fff;font-family:"Arimo",Arial,sans-serif;color:var(--text)}
.abs{position:absolute}

/* header */
.site-header{position:absolute;left:0;top:0;width:1200px;height:105px;background:#fff}
.brand{position:absolute;left:66px;top:26px;display:flex;align-items:center;gap:14px}
.brand-mark{width:40px;height:40px;background:var(--deep)}
.brand-name{font-family:"Arimo",sans-serif;font-weight:700;font-size:22px;color:var(--deep);line-height:1.05;text-transform:uppercase}
.top-bar{position:absolute;right:0;top:0;width:466px;height:42px;background:var(--deep);clip-path:polygon(30px 0,100% 0,100% 100%,0 100%,0 0);display:flex;align-items:center;justify-content:flex-end;gap:28px;padding-right:46px;color:#fff;font-size:15px}
.top-bar span{display:flex;align-items:center;gap:8px}
.main-nav{position:absolute;top:66px;left:808px;display:flex;gap:62px;font-size:17px;color:#222}
.main-nav a{color:inherit;text-decoration:none;padding-bottom:10px}
.main-nav a.active{border-bottom:3px solid var(--grey)}

/* hero */
.hero{position:absolute;left:0;top:105px;width:1200px;height:597px;background:linear-gradient(180deg,#8a96a4 0%,#5d6a79 45%,#2f3742 100%)}
.hero-copy{position:absolute;left:0;width:1200px;text-align:center;color:#fff;font-family:"Montserrat",sans-serif}
.hero-kicker{top:207px;font-weight:300;font-size:42px}
.hero-title{top:253px;font-weight:600;font-size:51px}
.btn-primary{position:absolute;left:513px;top:337px;width:177px;height:50px;background:var(--deep);color:#fff;font-size:15px;display:flex;align-items:center;justify-content:center;border-radius:2px}

/* search */
.search{position:absolute;left:0;top:702px;width:1200px;height:448px;background:var(--light)}
.search-intro{position:absolute;left:101px;top:86px;width:290px}
.search-intro .eyebrow{font-family:"Montserrat",sans-serif;font-weight:600;font-size:17px;color:#222}
.search-intro h2{font-family:"Montserrat",sans-serif;font-weight:700;font-size:32px;color:#222;margin-top:8px;letter-spacing:.5px}
.search-intro .tag{font-size:17px;color:var(--mid);margin-top:8px}
.search-intro p{font-size:13px;line-height:1.6;color:var(--grey);margin-top:18px}
.field{position:absolute;background:#fff;height:51px;display:flex;align-items:center;padding:0 16px;font-size:13px;color:#555;border:1px solid #e2e2e2}
.field.select::after{content:"";position:absolute;right:14px;top:22px;border:5px solid transparent;border-top:6px solid #222}
.range-label{position:absolute;font-size:12px;color:#333}
.range-track{position:absolute;height:5px;background:#bfc4c9}
.range-track i{position:absolute;top:-5px;width:14px;height:14px;background:var(--mid)}
.range-val{position:absolute;font-size:10px;color:#555}
.check{position:absolute;left:506px;top:322px;font-size:12px;color:#222;display:flex;gap:8px;align-items:center}
.btn-dark{position:absolute;left:973px;top:321px;width:142px;height:43px;background:#222;color:#fff;font-size:12px;font-weight:700;display:flex;align-items:center;justify-content:center;border-radius:3px;letter-spacing:.5px}

/* section headings */
.section-title{position:absolute;left:0;width:1200px;text-align:center;font-family:"Arimo",sans-serif;font-size:44px;font-weight:400;color:#333;letter-spacing:1px}
.divider{position:absolute;left:515px;width:170px;height:20px}

.about-text{position:absolute;left:72px;top:1283px;width:1056px;text-align:center;font-size:14.5px;line-height:1.55;color:#333}

/* sectors */
.sectors-band{position:absolute;left:0;top:1572px;width:1200px;height:473px;background:linear-gradient(180deg,#2b2420 0%,#1e1a18 60%,#2a241f 100%)}
.sector-img{position:absolute;top:1410px;width:342px;height:162px}
.sector-card{position:absolute;top:1572px;width:342px;height:194px;color:#fff;text-align:center;padding:20px 26px}
.sector-card h3{font-size:28px;font-weight:400;letter-spacing:1px}
.sector-card p{font-size:14px;line-height:1.5;margin-top:10px}
.card-grey{background:var(--grey)}
.card-navy{background:var(--ink)}
.cta-kicker{position:absolute;left:0;top:1808px;width:1200px;text-align:center;color:#fff;font-family:"Roboto Condensed",sans-serif;font-weight:300;font-size:38px;letter-spacing:2px}
.cta-title{position:absolute;left:0;top:1862px;width:1200px;text-align:center;color:#fff;font-family:"Roboto Condensed",sans-serif;font-weight:700;font-size:52px;letter-spacing:1px}
.btn-grey{position:absolute;left:508px;top:1952px;width:182px;height:52px;background:var(--grey);color:#fff;font-size:16px;display:flex;align-items:center;justify-content:center;border-radius:3px}

/* portfolio */
.tile{position:absolute;width:333px;height:221px}
.tile-overlay{position:absolute;left:10px;top:10px;right:10px;bottom:10px;border:1px solid rgba(255,255,255,.8)}
.tile-title{position:absolute;left:20px;top:24px;color:#fff;font-family:"Montserrat",sans-serif;font-weight:700;font-size:14px;line-height:1.5}
.tile-btn{position:absolute;left:100px;top:150px;width:134px;height:38px;border:2px solid #fff;color:#fff;font-size:14px;display:flex;align-items:center;justify-content:center;letter-spacing:.5px}
.tile-heart{position:absolute;right:24px;top:22px}

/* contact */
.contact{position:absolute;left:0;top:2765px;width:1200px;height:471px;background:#4a4a4a;color:#fff;font-family:"Open Sans",sans-serif}
.contact h2{position:absolute;left:78px;top:76px;font-family:"EB Garamond",serif;font-weight:500;font-size:36px;letter-spacing:1px}
.contact .lead{position:absolute;left:80px;top:126px;width:560px;font-size:15px;line-height:1.2}
.info{position:absolute;left:78px;display:flex;align-items:center;gap:16px;font-size:14px;line-height:1.25}
.info .ico{width:42px;height:42px;border-radius:50%;background:#fff;display:flex;align-items:center;justify-content:center;flex:none}
.input{position:absolute;left:495px;width:262px;height:42px;border:1px solid #ddd;padding:12px 14px;font-size:14px}
.message{position:absolute;left:778px;top:210px;width:317px;height:154px;border:1px solid #ddd;padding:10px 14px;font-size:14px}
.btn-submit{position:absolute;left:495px;top:378px;width:111px;height:42px;background:#262626;color:#fff;font-size:14px;display:flex;align-items:center;justify-content:center}
.site-footer{position:absolute;left:0;top:3236px;width:1200px;height:67px;background:var(--footer);color:#fff;font-family:"Open Sans",sans-serif;font-size:14px;display:flex;align-items:center;justify-content:center}
</style>
</head>
<body>

<header class="site-header">
  <div class="brand"><div class="brand-mark"></div><div class="brand-name">Norvale<br>Property<br>Management</div></div>
  <div class="top-bar">
    <span><svg width="15" height="15" viewBox="0 0 24 24"><path fill="#fff" d="M6.6 10.8a15 15 0 0 0 6.6 6.6l2.2-2.2c.3-.3.7-.4 1-.2 1.1.4 2.3.6 3.6.6.6 0 1 .4 1 1V20c0 .6-.4 1-1 1A17 17 0 0 1 3 4c0-.6.4-1 1-1h3.5c.6 0 1 .4 1 1 0 1.3.2 2.5.6 3.6.1.3 0 .7-.2 1z"/></svg>715.555.0148</span>
    <span><svg width="17" height="13" viewBox="0 0 24 18"><rect width="24" height="18" fill="#fff"/><path d="M1 1l11 9 11-9" stroke="#0b3470" stroke-width="2" fill="none"/></svg>hello@norvalepm.com</span>
  </div>
  <nav class="main-nav"><a class="active">Services</a><a>About Us</a><a>Contact</a></nav>
</header>

<section class="hero" role="img" aria-label="Upward view of glass office towers against a cloudy sky">
  <div class="hero-copy hero-kicker">We Build Perfect</div>
  <div class="hero-copy hero-title">Website For Your Business</div>
  <div class="btn-primary">View Our Projects</div>
</section>

<section class="search">
  <div class="search-intro">
    <div class="eyebrow">Find Your Dream</div>
    <h2>RENT PROPERTY</h2>
    <div class="tag">Anytime, Anywhere!</div>
    <p>Vestibulum at magna tellus. Vivamus sagittis et nunc ut in orci aliquam, ac vulputate leo vehicula. Mauris porttit magna tellus. Vivamus sagittis et nunc ut in orci aliquam iiculta. Donec eget ultricies ipsencon. Vestibulum at ma gna tellus. Vivamus sagittis et nunc utin orci</p>
  </div>
  <div class="field" style="left:506px;top:90px;width:425px">Where Do You Want To Live?</div>
  <div class="field select" style="left:930px;top:90px;width:185px">Property Location</div>
  <div class="field select" style="left:506px;top:160px;width:194px">Minimum Baths</div>
  <div class="field select" style="left:712px;top:160px;width:194px">Property Type</div>
  <div class="field select" style="left:918px;top:160px;width:197px">Minimum Beds</div>

  <div class="range-label" style="left:506px;top:234px">Price Range</div>
  <div class="range-label" style="left:682px;top:234px">£22,000 - £93,000</div>
  <div class="range-track" style="left:506px;top:266px;width:284px"><i style="left:0"></i><i style="right:0"></i></div>
  <div class="range-val" style="left:506px;top:281px">22000 £</div>
  <div class="range-val" style="left:744px;top:281px">93000 £</div>

  <div class="range-label" style="left:838px;top:234px">Area Range</div>
  <div class="range-label" style="left:996px;top:234px">99 sq ft - 2229 sq ft</div>
  <div class="range-track" style="left:838px;top:266px;width:270px"><i style="left:0"></i><i style="right:0"></i></div>
  <div class="range-val" style="left:838px;top:281px">99 sq ft</div>
  <div class="range-val" style="left:1053px;top:281px">2229 sq ft</div>

  <div class="check"><svg width="12" height="10" viewBox="0 0 12 10"><path d="M1 5l3.5 3.5L11 1" stroke="#222" stroke-width="2" fill="none"/></svg>Find Your Property Online</div>
  <div class="btn-dark">SEARCH NOW</div>
</section>

<h2 class="section-title" style="top:1190px">ABOUT NORVALE</h2>
<svg class="divider" style="top:1246px" viewBox="0 0 170 20"><line x1="0" y1="12" x2="70" y2="12" stroke="#0b3470" stroke-width="1.5"/><line x1="100" y1="12" x2="170" y2="12" stroke="#0b3470" stroke-width="1.5"/><rect x="78" y="3" width="14" height="14" fill="none" stroke="#333" stroke-width="2"/></svg>
<p class="about-text">FAR FAR AWAY, behind the word mountains, far from the countries Vokalia and Consonantia, there live the blind texts. Separated they live in Bookmarksgrove right at the coast of the Semantics, a large language ocean.Far far away, behind the word mountains, far from the countries VOKALIA AND CONSONANTIA, there live the blind texts.</p>

<section class="sectors-band" role="img" aria-label="Dim interior of a modern kitchen"></section>
<div class="sector-img" style="left:88px;background:linear-gradient(180deg,#6fa0d6 0%,#c9d3dc 50%,#5f8f3d 100%)" role="img" aria-label="Row of suburban houses on a green lawn"></div>
<div class="sector-img" style="left:431px;background:linear-gradient(180deg,#8fb2d8 0%,#b98a5c 55%,#6f7c3f 100%)" role="img" aria-label="Commercial shopping street with arcades"></div>
<div class="sector-img" style="left:774px;background:linear-gradient(180deg,#3a4a8a 0%,#8a4a6a 55%,#d98a3a 100%)" role="img" aria-label="Industrial plant lit at dusk"></div>
<div class="sector-card card-grey" style="left:88px"><h3>RESIDENTIAL</h3><p>FAR FAR AWAY, behind the word mountains, far from the countries Vokalia and Consonantia, there live the blind texts Separated they live in Bookmarksgrove</p></div>
<div class="sector-card card-navy" style="left:431px"><h3>COMMERCIAL</h3><p>FAR FAR AWAY, behind the word mountains, far from the countries Vokalia and Consonantia, there live the blind texts Separated they live in Bookmarksgrove</p></div>
<div class="sector-card card-grey" style="left:774px"><h3>INDUSTRIAL</h3><p>FAR FAR AWAY, behind the word mountains, far from the countries Vokalia and Consonantia, there live the blind texts Separated they live in Bookmarksgrove</p></div>
<div class="cta-kicker">Successfully Delivering Projects</div>
<div class="cta-title">FOR NEW AND REPEAT CLIENTS</div>
<div class="btn-grey">Get Free Estimate!</div>

<h2 class="section-title" style="top:2072px">ESTATE PORTFOLIO</h2>
<svg class="divider" style="top:2140px" viewBox="0 0 170 20"><line x1="0" y1="12" x2="70" y2="12" stroke="#0b3470" stroke-width="1.5"/><line x1="100" y1="12" x2="170" y2="12" stroke="#0b3470" stroke-width="1.5"/><rect x="78" y="3" width="14" height="14" fill="none" stroke="#333" stroke-width="2"/></svg>

<div class="tile" style="left:74px;top:2203px;background:linear-gradient(180deg,#3d3d3d,#262626)" role="img" aria-label="Two-storey house at dusk, darkened">
  <div class="tile-overlay"></div>
  <div class="tile-title">SUBWAY ELEVATION<br>CALIFORNIA</div>
  <svg class="tile-heart" width="32" height="28" viewBox="0 0 32 28"><path d="M16 26S2 17 2 9a7 7 0 0 1 14-2 7 7 0 0 1 14 2c0 8-14 17-14 17z" fill="none" stroke="#fff" stroke-width="2"/></svg>
  <div class="tile-btn">VIEW MORE</div>
</div>
<div class="tile" style="left:434px;top:2203px;background:linear-gradient(180deg,#e9e6df 0%,#d8d4cb 55%,#6b4a33 100%)" role="img" aria-label="Bright bathroom with white vanity"></div>
<div class="tile" style="left:795px;top:2203px;background:linear-gradient(180deg,#bcd0de 0%,#e8e2dc 60%,#8a6a4a 100%)" role="img" aria-label="Child's bedroom with colourful bedding"></div>
<div class="tile" style="left:74px;top:2453px;background:linear-gradient(180deg,#8fb0d4 0%,#2e2a2a 55%,#556b3a 100%)" role="img" aria-label="Dark-roofed family home with front lawn"></div>
<div class="tile" style="left:434px;top:2453px;background:linear-gradient(180deg,#d9d4cc 0%,#8f8275 50%,#3a2e28 100%)" role="img" aria-label="Living room with stone fireplace"></div>
<div class="tile" style="left:795px;top:2453px;background:linear-gradient(180deg,#f2f2f2 0%,#a08f7c 55%,#6f6a60 100%)" role="img" aria-label="Stone and timber house with double garage"></div>

<section class="contact">
  <h2>GET IN TOUCH</h2>
  <p class="lead">We are very approachable and would love to speak to you. Feel free to call, send us an email, Tweet us or simply complete the enquiry form.</p>
  <div class="info" style="top:203px"><div class="ico"><svg width="16" height="22" viewBox="0 0 16 22"><path d="M8 0a8 8 0 0 0-8 8c0 6 8 14 8 14s8-8 8-14a8 8 0 0 0-8-8z" fill="#0555a3"/><circle cx="8" cy="8" r="3" fill="#fff"/></svg></div><span>Alberta, Canada, offering services<br>Alberta wide</span></div>
  <div class="info" style="top:272px"><div class="ico"><svg width="20" height="15" viewBox="0 0 24 18"><rect x="1" y="1" width="22" height="16" fill="none" stroke="#0555a3" stroke-width="2"/><path d="M1 1l11 9 11-9" stroke="#0555a3" stroke-width="2" fill="none"/></svg></div><span>info@norvalepm.com</span></div>
  <div class="info" style="top:341px"><div class="ico"><svg width="18" height="18" viewBox="0 0 24 24"><path fill="#0555a3" d="M6.6 10.8a15 15 0 0 0 6.6 6.6l2.2-2.2c.3-.3.7-.4 1-.2 1.1.4 2.3.6 3.6.6.6 0 1 .4 1 1V20c0 .6-.4 1-1 1A17 17 0 0 1 3 4c0-.6.4-1 1-1h3.5c.6 0 1 .4 1 1 0 1.3.2 2.5.6 3.6.1.3 0 .7-.2 1z"/></svg></div><span>+44-xxxxxxxxxxxxx</span></div>
  <div class="input" style="top:213px">Name</div>
  <div class="input" style="top:268px">Number</div>
  <div class="input" style="top:322px">Mail</div>
  <div class="message">Message</div>
  <div class="btn-submit">SUBMIT</div>
</section>

<footer class="site-footer">All rights reserved Copyright © 2017 Ridgeway Web Studio</footer>

</body>
</html>
```